Pelbrook Business Cards

Create new business cards with the details below.

Aaron Velst
Director

MB: +61 412 563 904
PH: 1300 417 639
Email: aaron.velst@pelbrook.com.au
Address: 27C Marlow Parade, Harrowfield VIC 3094 Australia
Website: www.pelbrook.com.au

Target Market(s)

Other business

Industry/Entity Type

Business

Requirements
Must have
• must be clean looking

```html
<!DOCTYPE html>
<html lang="en">
<head>
<meta charset="utf-8">
<title>Pelbrook Business Card</title>
<link rel="stylesheet" href="https://fonts.googleapis.com/css2?family=Montserrat:wght@600;700&family=Roboto:wght@300;400;500&display=swap">
<style>
  :root {
    --backdrop: #1c1c1c;
    --accent-green: #a6d22e;
    --band-dark: #2a2a2a;
    --band-dark-edge: #3a3a3a;
    --wood-light: #d9d9d7;
    --wood-mid: #c4c4c2;
    --wood-deep: #b3b3b1;
    --ink-dark: #2b2b2b;
    --ink-soft: #4a4a4a;
  }
  * { margin: 0; padding: 0; box-sizing: border-box; }
  html, body {
    width: 1200px;
    height: 801px;
    overflow: hidden;
    background: var(--backdrop);
  }
  .canvas {
    position: relative;
    width: 1200px;
    height: 801px;
  }
  .business-card {
    position: absolute;
    left: 150px;
    top: 140px;
    width: 900px;
    height: 520px;
    display: flex;
    overflow: hidden;
    box-shadow: 0 14px 40px rgba(0,0,0,0.55);
  }
  .accent-stripe {
    width: 77px;
    background: var(--accent-green);
  }
  .dark-band {
    width: 105px;
    background: linear-gradient(90deg, var(--band-dark) 0%, var(--band-dark-edge) 100%);
  }
  .card-face {
    position: relative;
    flex: 1;
  }
  .wood-surface {
    position: absolute;
    inset: 0;
    background: linear-gradient(180deg, var(--wood-light) 0%, var(--wood-mid) 55%, var(--wood-deep) 100%);
  }
  .brand {
    position: absolute;
    left: 68px;
    top: 36px;
  }
  .brand-row {
    display: flex;
    align-items: center;
    gap: 16px;
  }
  .brand-square {
    width: 72px;
    height: 72px;
    background: var(--ink-dark);
  }
  .brand-name {
    font-family: "Montserrat", sans-serif;
    font-weight: 700;
    font-size: 80px;
    letter-spacing: 1px;
    line-height: 1;
    color: var(--ink-dark);
  }
  .brand-tagline {
    margin-top: 8px;
    margin-left: 88px;
    font-family: "Montserrat", sans-serif;
    font-weight: 600;
    font-size: 32px;
    letter-spacing: 3px;
    line-height: 1.1;
    color: var(--ink-dark);
  }
  .person {
    position: absolute;
    left: 180px;
    top: 238px;
    font-family: "Roboto", sans-serif;
  }
  .person-name {
    font-weight: 300;
    font-size: 34px;
    color: var(--ink-soft);
  }
  .person-title {
    font-weight: 500;
    font-size: 24px;
    color: var(--ink-dark);
    margin-top: 2px;
  }
  .contact {
    position: absolute;
    left: 178px;
    top: 380px;
    display: flex;
    align-items: center;
    gap: 16px;
    font-family: "Roboto", sans-serif;
    font-size: 22px;
    color: var(--ink-dark);
  }
  .contact-icon {
    width: 30px;
    height: 52px;
    margin-top: 26px;
  }
  .contact-lines p { line-height: 1.3; }
  .contact-label { font-weight: 300; color: var(--ink-soft); }
  .address {
    position: absolute;
    left: 178px;
    top: 480px;
    font-family: "Roboto", sans-serif;
    font-weight: 300;
    font-size: 19px;
    color: var(--ink-dark);
  }
</style>
</head>
<body>
<main class="canvas">
  <article class="business-card">
    <div class="accent-stripe"></div>
    <div class="dark-band"></div>
    <section class="card-face">
      <div class="wood-surface" role="img" aria-label="Weathered light grey timber plank texture"></div>

      <div class="brand">
        <div class="brand-row">
          <span class="brand-square"></span>
          <span class="brand-name">PELBROOK</span>
        </div>
        <div class="brand-tagline">PLANTATION SHUTTERS</div>
      </div>

      <div class="person">
        <p class="person-name">Aaron Velst</p>
        <p class="person-title">Director</p>
      </div>

      <div class="contact">
        <svg class="contact-icon" viewBox="0 0 30 52" aria-hidden="true">
          <rect x="2" y="2" width="26" height="48" rx="4" fill="none" stroke="#2b2b2b" stroke-width="2.5"/>
          <line x1="2" y1="9" x2="28" y2="9" stroke="#2b2b2b" stroke-width="2"/>
          <line x1="2" y1="41" x2="28" y2="41" stroke="#2b2b2b" stroke-width="2"/>
          <circle cx="15" cy="45.5" r="2" fill="#2b2b2b"/>
        </svg>
        <div class="contact-lines">
          <p>aaron.velst@pelbrook.com.au</p>
          <p><span class="contact-label">MB:</span> +61 412 563 904</p>
          <p><span class="contact-label">PH:</span> 1300 417 639</p>
        </div>
      </div>

      <p class="address">27C Marlow Parade, Harrowfield VIC 3094, Australia</p>
    </section>
  </article>
</main>
</body>
</html>
```